Calloway needs a modernized design

We would like a modern update (that can be responsive) to our existing website. Attached are the two existing pages we would like new concepts of - our home page and a page about one of our locations.

Calloway is provides executive offices and virtual office services. Startups, law firms, and financial services are our primary clients. We would like a professional, clean design, leaning towards minimalist. We intend to greatly reduce/eliminate the long paragraphs of text.

Industry/Entity Type

Business Service

Number of Pages Required

2 page

Requirements
Must have
• A design that can be responsive
Nice to have
• Large image(s) on home page that rotate.

```html
<!DOCTYPE html>
<html lang="en">
<head>
<meta charset="utf-8">
<title>Calloway Business Centers</title>
<link href="https://fonts.googleapis.com/css2?family=Open+Sans:wght@300;400;600;700&display=swap" rel="stylesheet">
<style>
:root{
  --navy:#2b3a67;
  --navy-footer:#2a3866;
  --navy-deep:#213058;
  --orange:#e8812a;
  --orange-btn:#ec7d22;
  --text:#555b66;
  --muted:#8a93ad;
  --line:#cfd3da;
  --white:#ffffff;
}
*{box-sizing:border-box;margin:0;padding:0}
html,body{width:1200px;height:2582px;overflow:hidden}
body{position:relative;font-family:"Open Sans",Arial,sans-serif;color:var(--text);background:var(--white)}
.abs{position:absolute}

.top-bar{left:0;top:0;width:1200px;height:41px;background:var(--navy);color:var(--white);font-size:13.5px;font-weight:600;text-align:right;padding:12px 112px 0 0}

.brand{left:110px;top:55px;display:flex;align-items:center;gap:12px}
.brand-mark{width:68px;height:68px;border-radius:50%;background:var(--navy)}
.brand-name{font-size:22px;font-weight:600;color:var(--navy);line-height:1.15;width:220px}

.social-top{left:962px;top:56px;display:flex;gap:10px}
.social-top span{width:14px;height:14px;border-radius:50%;background:var(--orange);display:block}

.main-nav{left:542px;top:100px;display:flex;gap:0;font-size:13.5px;color:#5a6172}
.main-nav a{color:inherit;text-decoration:none;margin-right:38px;padding-bottom:8px}
.main-nav a:last-child{margin-right:0}
.main-nav a.is-active{color:var(--orange);border-bottom:2px solid var(--orange)}

.hero-band{left:0;top:379px;width:1200px;height:516px;background:var(--navy)}
.hero-slide{left:70px;top:141px;width:1060px;height:563px;background:linear-gradient(135deg,#c9b8a6 0%,#e6ddd2 40%,#b9c2c9 70%,#8a6f5a 100%)}
.slide-dots{left:549px;top:582px;display:flex;gap:6px}
.slide-dots span{width:14px;height:14px;border-radius:50%;border:2px solid #fff;background:#222}
.slide-dots span.is-current{background:#fff}
.hero-caption{left:70px;top:616px;width:1060px;height:88px;background:rgba(45,45,50,.72)}
.hero-title{left:110px;top:628px;font-size:34px;font-weight:300;color:#fff;line-height:1.1}
.hero-sub{left:112px;top:670px;font-size:16px;color:#eee}
.btn-find{left:916px;top:637px;width:172px;height:48px;background:var(--orange-btn);color:#fff;font-size:17px;font-weight:600;text-align:center;line-height:48px;border-radius:3px}

.hero-tagline{left:260px;top:735px;width:680px;text-align:center;color:#fff;font-size:21.5px;font-weight:300;line-height:38px}

.value{left:110px;top:930px;width:980px;text-align:center}
.section-title{font-size:29px;font-weight:400;color:var(--orange)}
.value-lead{margin-top:8px;font-size:21px;line-height:31px;color:#4b4f58;font-weight:400}
.value-body{left:110px;top:1126px;width:980px;font-size:13.6px;line-height:22px;color:#6b7080}
.value-body p{margin-bottom:22px}

.community-band{left:0;top:1391px;width:1200px;height:409px;background:var(--orange)}
.band-col{top:1424px;width:479px;color:#fff}
.band-col h2{font-size:32px;font-weight:400;margin-bottom:8px}
.band-col p{font-size:13.6px;line-height:26px;margin-bottom:26px;color:#fff3e6}
.col-community{left:110px}
.col-service{left:611px;text-align:justify}

.request-title{left:110px;top:1830px;font-size:32px;font-weight:300;color:var(--orange)}
.field{width:307px}
.field label{display:block;font-size:14px;color:#5a5f6a;margin-bottom:5px}
.field .input{height:38px;border:1px solid var(--line);border-radius:3px;background:#fff;position:relative}
.field .input svg{position:absolute;right:12px;top:15px}
.btn-submit{left:444px;top:2168px;width:171px;height:47px;background:var(--orange-btn);color:#fff;font-size:17px;font-weight:600;text-align:center;line-height:47px;border-radius:3px}
.special-card{left:780px;top:1837px;width:308px;height:300px;background:linear-gradient(180deg,#f2b46c 0%,#e9a461 55%,#d89a66 100%)}
.special-label{left:780px;top:1958px;width:308px;text-align:center;color:#fff;font-size:30px;font-weight:300;line-height:30px}

.site-footer{left:0;top:2273px;width:1200px;height:258px;background:var(--navy-footer)}
.footer-bottom{left:0;top:2531px;width:1200px;height:51px;background:var(--navy-deep);color:var(--muted);font-size:12px;padding:18px 0 0 110px}
.footer-head{top:2313px;font-size:16.5px;font-weight:600;color:#fff}
.footer-list{top:2360px;list-style:none;font-size:12px;color:var(--muted);line-height:31px}
.social-list li{display:flex;align-items:center;gap:12px}
.social-list li span{width:16px;height:16px;border-radius:50%;background:#8e99b8;display:block}
.office{left:697px;top:2360px;font-size:12px;line-height:21px;color:var(--muted)}
.office strong{color:#c2c9dc;font-weight:600}
.badge{left:934px;top:2339px;width:154px;height:154px;border-radius:50%;background:#dfe3ec;border:8px solid #56658f}
</style>
</head>
<body>

<div class="abs top-bar">Dallas 214.555.0142 | Houston 713.555.0187</div>

<div class="abs brand">
  <div class="brand-mark"></div>
  <div class="brand-name">Calloway Business Centers</div>
</div>

<div class="abs social-top" aria-label="Social links">
  <span></span><span></span><span></span><span></span><span></span>
</div>

<nav class="abs main-nav">
  <a class="is-active" href="#">Home</a>
  <a href="#">Properties</a>
  <a href="#">Virtual Tours &amp; Videos</a>
  <a href="#">Photos</a>
  <a href="#">Broker Referrals</a>
</nav>

<div class="abs hero-band"></div>
<div class="abs hero-slide" role="img" aria-label="Young professionals gathered around a laptop at a shared office desk"></div>
<div class="abs slide-dots"><span class="is-current"></span><span></span><span></span><span></span><span></span></div>
<div class="abs hero-caption"></div>
<div class="abs hero-title">Executive Office Suites</div>
<div class="abs hero-sub">Professional Office Space Solutions. One Low Cost.</div>
<div class="abs btn-find">Find More</div>

<p class="abs hero-tagline">Come See Why Smarter Businesses Are Choosing Calloway Business Centers' Dallas, Ft. Worth and Houston Executive Office Suites, Virtual Offices, Meeting Rooms and Video Conferencing.</p>

<section class="abs value">
  <h2 class="section-title">Value</h2>
  <p class="value-lead">Either you need Dallas/Ft. Worth Office Space, Dallas Executive Suites, Ft. Worth Executive Suites, Houston Office Space, Houston Executive Suites, or maybe you simply need a place to stop in and use an on-demand office or meeting room from time to time or utilize our local business phone numbers, phone answering or business addresses through one of our virtual office solutions.</p>
</section>

<div class="abs value-body">
  <p>At Calloway, you will always find affordable and beautiful, professional properties. To make decisions easy for our full service executive suite clients, we include everything in one upfront and honest price - including the office, phone answering and 55 hours of conference room time per month (alone a value of over $1,600/mo).</p>
  <p>Our meeting room, training room, computer lab, conference room, board room and video conference room rentals are another tribute to that same philosophy of value. We will not charge you booking fees, service fees or administrative fees and parking is free at every location.</p>
  <p>Added value is found in our flexibility and comprehensive service offerings. Starting or growing a business is difficult enough and renting your office, virtual office or meeting room shouldn't be. We can help you scale your space as quickly as needed, depending upon your requirement. Start with an on-demand office or meeting room and as your business scales, grow into a virtual office and then a Full Service office.</p>
</div>

<div class="abs community-band"></div>
<section class="abs band-col col-community">
  <h2>Community</h2>
  <p>Companies that partner with Calloway share more than a prestigious address. They also share ideas and services. Our Executive Office Business Centers are places where savvy, growing companies can network, interact and learn from one another.</p>
  <p>We are also a large part of the community within our home state of Texas. We have been a contributing business member for 15 years, and are proud to say we have built a solid reputation as an upstanding member of the Dallas, Ft. Worth and Houston business communities by honoring our commitments.</p>
</section>
<section class="abs band-col col-service">
  <h2>Service</h2>
  <p>The service we provide in terms of technology is unparalleled in our industry. We outfit each of our locations with 100Mbps of bandwidth! We have the latest systems in place, with all locations offering IP PBX telephone systems, Corvane IP telephones and RingAlong Technology including Voicemail to Email and FaxLine, with local technical support. All of this is in place to ensure you can operate your business with maximum efficiency.</p>
  <p>Our customers begin their road to profitability with Calloway and stay for extended terms. Our customers know that we will manage every aspect of the workplace, so they can focus their time and energy on running their businesses.</p>
</section>

<h2 class="abs request-title">Request Information</h2>

<div class="abs field" style="left:110px;top:1910px"><label>First Name</label><div class="input"></div></div>
<div class="abs field" style="left:444px;top:1910px"><label>Email</label><div class="input"></div></div>
<div class="abs field" style="left:110px;top:1987px"><label>Last Name</label><div class="input"></div></div>
<div class="abs field" style="left:444px;top:1987px"><label>Property Interested In</label><div class="input"><svg width="10" height="6" viewBox="0 0 10 6"><path d="M0 0h10L5 6z" fill="#333"/></svg></div></div>
<div class="abs field" style="left:110px;top:2064px"><label>Company Name</label><div class="input"></div></div>
<div class="abs field" style="left:444px;top:2064px"><label>Product Interested In</label><div class="input"><svg width="10" height="6" viewBox="0 0 10 6"><path d="M0 0h10L5 6z" fill="#333"/></svg></div></div>
<div class="abs field" style="left:110px;top:2141px"><label>Phone Number</label><div class="input"></div></div>
<div class="abs btn-submit">Submit</div>

<div class="abs special-card" role="img" aria-label="Sunlit conference room with a table and chairs, tinted orange"></div>
<div class="abs special-label">View Current<br>Special</div>

<footer class="abs site-footer"></footer>
<div class="abs footer-head" style="left:110px">Main Links</div>
<ul class="abs footer-list" style="left:110px">
  <li>About Us</li><li>Contact Us</li><li>Forms</li><li>Testimonials</li><li>FAQs</li>
</ul>
<ul class="abs footer-list" style="left:277px">
  <li>Careers</li><li>Furniture</li><li>Specials</li><li>Site Map</li><li>Privacy</li>
</ul>
<div class="abs footer-head" style="left:444px">Social Media</div>
<ul class="abs footer-list social-list" style="left:444px">
  <li><span></span>Video Channel</li>
  <li><span></span>Microblog</li>
  <li><span></span>Circles</li>
  <li><span></span>Pro Network</li>
  <li><span></span>Pinboard</li>
</ul>
<div class="abs footer-head" style="left:697px">Corporate Office</div>
<address class="abs office" style="font-style:normal">
  Calloway Business Centers<br>4120 Lakeside Parkway<br>Suite 300<br>Dallas, Texas 75219<br><br>
  <strong>Dallas 214.555.0142</strong><br><strong>Houston 713.555.0187</strong>
</address>
<div class="abs badge" role="img" aria-label="Anniversary badge"></div>

<div class="abs footer-bottom">Copyright 2016 Calloway Business Centers All Rights Reserved</div>

</body>
</html>
```